Riverbend Trusted Home Care-Flyer for Patients

Our Home Health Care Agency, Riverbend Trusted Home Care, is seeking a flyer to advertise our services. We would like our flyer to convey professionalism, classiness and sophistication. We want our agency to come across as one that is well-established and recognized as being first-rate within the field.

We also want to appear original; we want to stand out.

Our theme colors, blue and green, from our logo should be incorporated into the flyer's design (refer below).

The top of the page should say (in a clear, bold font)-Seeking Care for your Loved One?

Our Logo, followed by our slogan, "Lean On Those Nearby", should be in the center. (This should make it appear as if our agency is the obvious solution to the consumer's quest in finding suitable care for their family member). This should be in a big font.
Below that, our agency's services should be listed in a very noticeable font...yet smaller than what's written above that.
The text should read:
Our Services Include:
*Experienced Certified Home Health Aides/ Live In Home Health Aides/Companions
*Nursing Services
*Alzheimer’s and Dementia Care
*Respite Care
*Postoperative Care
*Post Rehabilitation Care
*Running Errands
*Light Housekeeping
*Assistance with Bathing, Feeding and Grooming
*Meal Preparation
*Laundry and Linen Washing
*Mail and Bill Organization
*Medication Management
*Accompanying to Doctor’s Appointments
*And much more!
Below that, in a smaller, yet noticeable font:
As seasoned professionals, we know how to help our clients navigate and fulfill their various health care needs. Those nearby are here to help you get the attention that you merit.
Call Riverbend Trusted Home Care today to learn more about our first-rate services!
Below that, in a larger font, our phone number, website, our e-mail address.
*Out contact information will be provided to the project’s winner*.

*Pictures of Caregivers helping elderly patient should be included in the advertisement as well. *

We provided advertisements of other Home Health Care Agencies attached below to use as a reference. Once again, while we are aiming for a similar idea; however, our goal is to stand out as the community's premiere home health care agency, the one that they want to choose. We want to be original as well!

Size: Standard Computer Paper Size. 8.5” x 11”.

Feel free to utilize your creative, designer flair!
We look forward to seeing the results!
Good luck!

Industry/Entity Type

Home Health Care

Font styles to use
Sans Serif

Requirements
Must have
• Refer above.
Nice to have
• Refer to attachment below to see how other home health care agencies advertise. While we are aiming for a similar idea, we would like to incorporate our logo, slogan and colors to make this flyer more unique and stand out. We would like to appear original.

```html
<!DOCTYPE html>
<html lang="en">
<head>
<meta charset="utf-8">
<title>Riverbend Trusted Home Care – Flyer</title>
<link rel="stylesheet" href="https://fonts.googleapis.com/css2?family=Arimo:wght@400;700&family=Cabin:wght@500&display=swap">
<style>
  :root{
    --blue:#114c97;
    --blue-dark:#0c3f82;
    --green:#7cc242;
    --green-deep:#4d9f2a;
    --green-light:#bfe39a;
    --white:#ffffff;
    --ink:#1d1d1f;
    --page-bg:#e9e6e1;
  }
  *{margin:0;padding:0;box-sizing:border-box}
  html,body{width:1200px;height:939px;overflow:hidden;background:var(--page-bg)}
  .flyer{position:absolute;left:250px;top:16px;width:700px;height:906px;background:var(--white);overflow:hidden;font-family:"Arimo",Arial,sans-serif;box-shadow:0 2px 10px rgba(0,0,0,.15)}
  .shapes{position:absolute;left:0;top:0}
  .hero-photo{position:absolute;left:250px;top:0;width:450px;height:380px;
    background:linear-gradient(90deg,rgba(255,255,255,1) 0%,rgba(236,228,220,.6) 22%,rgba(220,205,192,.9) 55%,#e8d9cf 100%),
    linear-gradient(180deg,#f1ebe3 0%,#c7d3e6 60%,#a9bfe0 100%)}
  .brand{position:absolute;left:56px;top:48px;width:200px;text-align:center;color:var(--blue)}
  .brand-dot{width:52px;height:52px;border-radius:50%;border:4px solid var(--green);margin:0 auto 8px}
  .brand-name{font-weight:700;font-size:15px;line-height:17px;letter-spacing:.3px;text-transform:uppercase}
  .headline{position:absolute;left:17px;top:176px;color:var(--blue);font-weight:700;font-size:28px;line-height:30px}
  .headline-accent{position:absolute;left:17px;top:200px;color:var(--green);font-weight:700;font-size:42px;line-height:46px}
  .slogan{position:absolute;left:0;top:254px;width:287px;height:49px;background:var(--green);border-radius:0 26px 26px 0;
    box-shadow:0 3px 3px rgba(0,0,0,.15);color:var(--blue);font-weight:700;font-size:20px;line-height:21px;padding:4px 0 0 19px;text-transform:uppercase}
  .circle-photo{position:absolute;left:9px;top:323px;width:150px;height:150px;border-radius:50%;border:4px solid var(--blue);
    background:radial-gradient(circle at 50% 60%,#b9b2ad 0%,#7d8a6a 55%,#3f6a2e 100%)}
  .services-title{position:absolute;left:271px;top:406px;width:214px;height:41px;border-radius:21px;background:var(--blue);
    color:var(--white);font-weight:700;font-size:27px;line-height:41px;text-align:center}
  .service-list{position:absolute;list-style:none;font-family:"Cabin",Arial,sans-serif;font-weight:500;font-size:13px;line-height:16.5px;color:var(--white)}
  .service-list li{position:absolute;left:0;white-space:nowrap}
  .service-list svg{position:absolute;left:-19px;top:2px}
  .service-list.left{left:90px;top:0}
  .service-list.right{left:434px;top:0}
  .divider{position:absolute;left:367px;top:491px;width:2px;height:214px;background:var(--white)}
  .about{position:absolute;left:33px;top:805px;width:420px;color:var(--white);font-size:12.4px;line-height:15px}
  .contact{position:absolute;left:506px;top:796px;list-style:none;color:var(--ink);font-size:12.5px}
  .contact li{position:relative;height:27px;padding-left:16px;line-height:15px}
  .contact svg{position:absolute;left:0;top:2px}
</style>
</head>
<body>
<main class="flyer">
  <div class="hero-photo" role="img" aria-label="Photo of a caregiver in pink scrubs hugging a smiling elderly woman on a sofa"></div>

  <svg class="shapes" width="700" height="906" viewBox="0 0 700 906" aria-hidden="true">
    <defs>
      <radialGradient id="greenField" cx="0.55" cy="0.05" r="0.9">
        <stop offset="0" stop-color="var(--green-light)"/>
        <stop offset="0.5" stop-color="var(--green)"/>
        <stop offset="1" stop-color="var(--green-deep)"/>
      </radialGradient>
    </defs>
    <!-- top swoosh bands -->
    <path d="M0 420 Q330 330 700 355 L700 388 Q330 360 0 466 Z" fill="var(--blue)"/>
    <path d="M0 434 Q330 348 700 370 L700 378 Q330 356 0 446 Z" fill="var(--white)"/>
    <!-- green services field -->
    <path d="M0 462 Q330 358 700 388 L700 672 Q330 800 0 730 Z" fill="url(#greenField)"/>
    <!-- bottom bands -->
    <path d="M0 730 Q330 800 700 672 L700 690 Q330 812 0 742 Z" fill="var(--white)"/>
    <path d="M0 742 Q330 812 700 690 L700 906 L0 906 Z" fill="var(--blue)"/>
    <path d="M0 752 Q330 818 700 704 L700 714 Q330 824 0 760 Z" fill="var(--white)"/>
    <path d="M700 728 Q560 776 457 774 L488 906 L700 906 Z" fill="var(--white)"/>
  </svg>

  <header class="brand">
    <div class="brand-dot"></div>
    <p class="brand-name">Riverbend Trusted<br>Home Care</p>
  </header>

  <h1 class="headline">Seeking Care for your</h1>
  <p class="headline-accent">LOVED ONE?</p>
  <p class="slogan">Lean On Those<br>Nearby</p>

  <div class="circle-photo" role="img" aria-label="Photo of a smiling elderly man and a young caregiver giving thumbs up"></div>

  <h2 class="services-title">Our Services</h2>

  <ul class="service-list left">
    <li style="top:484px"><svg width="15" height="12" viewBox="0 0 15 12"><path d="M1 6 L5 10 L14 1" stroke="#fff" stroke-width="2.6" fill="none"/></svg>Experienced Certified Home Health Aides/<br>Live In Home Health Aides/Companions</li>
    <li style="top:527px"><svg width="15" height="12" viewBox="0 0 15 12"><path d="M1 6 L5 10 L14 1" stroke="#fff" stroke-width="2.6" fill="none"/></svg>Nursing Services</li>
    <li style="top:555px"><svg width="15" height="12" viewBox="0 0 15 12"><path d="M1 6 L5 10 L14 1" stroke="#fff" stroke-width="2.6" fill="none"/></svg>Alzheimer’s and Dementia Care</li>
    <li style="top:582px"><svg width="15" height="12" viewBox="0 0 15 12"><path d="M1 6 L5 10 L14 1" stroke="#fff" stroke-width="2.6" fill="none"/></svg>Respite Care</li>
    <li style="top:610px"><svg width="15" height="12" viewBox="0 0 15 12"><path d="M1 6 L5 10 L14 1" stroke="#fff" stroke-width="2.6" fill="none"/></svg>Postoperative Care</li>
    <li style="top:638px"><svg width="15" height="12" viewBox="0 0 15 12"><path d="M1 6 L5 10 L14 1" stroke="#fff" stroke-width="2.6" fill="none"/></svg>Post Rehabilitation Care</li>
    <li style="top:665px"><svg width="15" height="12" viewBox="0 0 15 12"><path d="M1 6 L5 10 L14 1" stroke="#fff" stroke-width="2.6" fill="none"/></svg>Running Errands</li>
    <li style="top:692px"><svg width="15" height="12" viewBox="0 0 15 12"><path d="M1 6 L5 10 L14 1" stroke="#fff" stroke-width="2.6" fill="none"/></svg>Light Housekeeping</li>
  </ul>

  <div class="divider"></div>

  <ul class="service-list right">
    <li style="top:482px"><svg width="15" height="12" viewBox="0 0 15 12"><path d="M1 6 L5 10 L14 1" stroke="#fff" stroke-width="2.6" fill="none"/></svg>Assistance with Bathing, Feeding<br>and Grooming</li>
    <li style="top:526px"><svg width="15" height="12" viewBox="0 0 15 12"><path d="M1 6 L5 10 L14 1" stroke="#fff" stroke-width="2.6" fill="none"/></svg>Meal Preparation</li>
    <li style="top:554px"><svg width="15" height="12" viewBox="0 0 15 12"><path d="M1 6 L5 10 L14 1" stroke="#fff" stroke-width="2.6" fill="none"/></svg>Laundry and Linen Washing</li>
    <li style="top:581px"><svg width="15" height="12" viewBox="0 0 15 12"><path d="M1 6 L5 10 L14 1" stroke="#fff" stroke-width="2.6" fill="none"/></svg>Mail and Bill Organization</li>
    <li style="top:609px"><svg width="15" height="12" viewBox="0 0 15 12"><path d="M1 6 L5 10 L14 1" stroke="#fff" stroke-width="2.6" fill="none"/></svg>Medication Management</li>
    <li style="top:636px"><svg width="15" height="12" viewBox="0 0 15 12"><path d="M1 6 L5 10 L14 1" stroke="#fff" stroke-width="2.6" fill="none"/></svg>Accompanying to Doctor’s<br>Appointments</li>
    <li style="top:680px"><svg width="15" height="12" viewBox="0 0 15 12"><path d="M1 6 L5 10 L14 1" stroke="#fff" stroke-width="2.6" fill="none"/></svg>And much more!</li>
  </ul>

  <p class="about">As seasoned professionals, we know how to help our clients navigate and fulfill their various health care needs. Those nearby are here to help you get the attention that you merit. Call Riverbend Trusted Home Care today to learn more about our first-rate services !</p>

  <ul class="contact">
    <li><svg width="11" height="11" viewBox="0 0 12 12"><circle cx="6" cy="6" r="5.3" fill="none" stroke="var(--green)" stroke-width="1.2"/><path d="M4 3.2 L5 5 L4.5 5.6 Q5.5 7.2 6.6 7.6 L7.2 7 L8.8 8 Q8 9.3 6.8 9 Q4 8 3.2 4.6 Q3.2 3.6 4 3.2Z" fill="var(--green)"/></svg>(555) 214 7780</li>
    <li><svg width="12" height="10" viewBox="0 0 12 10"><rect x="0.5" y="1" width="11" height="8" fill="var(--green)"/><path d="M0.5 1 L6 5.5 L11.5 1" stroke="#fff" fill="none"/></svg>hello@riverbendcare.example</li>
    <li><svg width="11" height="11" viewBox="0 0 12 12"><circle cx="6" cy="6" r="5.3" fill="none" stroke="var(--green)" stroke-width="1.2"/><ellipse cx="6" cy="6" rx="2.4" ry="5.3" fill="none" stroke="var(--green)"/><path d="M0.7 6 H11.3" stroke="var(--green)"/></svg>www.riverbendcare.example</li>
  </ul>
</main>
</body>
</html>
```